Travel postcards

We are looking for a highly talented graphic designer to create a set of 4 different 5x7 full color travel postcards designed to be mailed to prospective corporate clients to solicit upcoming events. Postcards will include photos and will be focused on European destinations and should be fun yet sophisticated.
Update 10/9/13: As these are postcards (not greeting cards) the designs should be based on a horizontal (not vertical) layout.
Updates

I updated the descriptions - please review updated description of project which elaborates more about what I'm looking for on the design of the cards.  Thank you.  Brent
Added Tuesday, October 08, 2013

Hello everyone,

fyi I uploaded some photos of Italy, a vellano logo and a photo of the Eiffel Tower today.  You do not have to use these photos, these are just suggestions and are photos we happen to have already.  I don't have any photos of Scotland yet, but I have requested photos from the Highland Visitors Council today and I will post them when I have them - or you can use other photos that you find if you prefer.                                   

Added Wednesday, October 09, 2013

Project Deadline Extended
Reason: need more time due to the delay in obtaining the last bunch of photos. also it appears that having a vellano for the entire time in italy maybe too far out of the trip budget and instead I might need to replace that idea with driving on the vellano test track for one day of the tour instead of having the vellano the whole time - I need time to investigate this further.
Added Thursday, October 10, 2013

Hello everyone - please remember to put the logo on the "back" of the postcard - not the front.  Also postcards should be horizontal, not vertical.  Thank you

Hi all - For the Scotland postcard it would be great to identify the golf courses with text as the people won't know what the photos are of without it.  thank you
Added Friday, October 11, 2013

Project Deadline Extended
Reason: I posted an update that the Vellano theme will no longer work for Italy but some designers are still submitting designs with the Vellano theme so I updated the specs. Also, designs for both sides of the postcard should be included, not just for the front of the card. thank you
Added Tuesday, October 22, 2013

Project Deadline Extended
Reason: Providing more time for revisions to be completed
Added Wednesday, October 30, 2013

Project Deadline Extended
Reason: need more time to review the designs
Added Tuesday, November 05, 2013

Target Market(s)

companies that distribute products to dealers, they take their customers who buy a lot of product from them away on these types of tripscompanies that distribute products to dealers, they take their customers who buy a lot of product from them away on these types of trips

Industry/Entity Type

Graphic Designer

Requirements
Must have
• Update: 10/8/13: A message on the front mentioning the theme of the trip such as "Custom wine tasting trip of France for your group with KWR Journeys" (I am not a writer so use a message that you feel fits the postcard). Also "Call 877-319-KWR7 (877-319-5977) for more details about our theme trips."

Update 10/17/13: Revised instructions for Italy postcard: I was advised that the Vellano factory tour is too difficult to arrange and too cost prohibitive. I am in the process of obtaining additional photos from the Tuscany region of Italy and will post these as soon as i have them. The Italy postcard should include photos of (1) either the Trevi Fountain or the Colisseum, (2) Villa Pieroluce in Tuscany (I am waiting for a high res photo), (3) San Giaminiamo and (4) statue of David... These are not necessarily in any particular order and your postcard should include at least 3 out of the 4 photos.
Nice to have
• Update: 10/8/13: Postcard should have 2-4 photos and they don't have to be equal sizes if more than one is used. Probably best not to use more than 4 photos on the card. I uploaded a photo of Manoir de Vessac that can be used for the France postcard.
Should not have
• Update 10/8/13: KWR logo should be on the back of the card. The logo isn't important enough for it to be on the front of the card.
Update 10/10/13: please remember to put the logo on the BACK of the postcard - not the front. Also postcards should be HORIZONTAL, not vertical. Thank you

```html
<!DOCTYPE html>
<html lang="en">
<head>
<meta charset="utf-8">
<title>Tour Italy in a Vellano – Postcard</title>
<link href="https://fonts.googleapis.com/css2?family=Gochi+Hand&display=swap" rel="stylesheet">
<style>
  :root {
    --backdrop: #141414;
    --card-grey: #d3d0cc;
    --card-grey-dark: #aaa6a2;
    --card-white: #ffffff;
    --tag-paper: #e8cc98;
    --tag-paper-dark: #c9a36a;
    --ink: #1e1a16;
    --ink-soft: #4a4540;
    --line-grey: #8c8c8c;
    --tyre-brown: rgba(150, 132, 112, .45);
    --sketch-tone: rgba(60, 55, 50, .16);
    --photo-frame: #f4f2ef;
  }
  * { box-sizing: border-box; margin: 0; padding: 0; }
  html, body {
    width: 1200px; height: 745px; overflow: hidden;
    background: var(--backdrop);
    font-family: "Gochi Hand", cursive;
  }
  .canvas { position: relative; width: 1200px; height: 745px; }

  .postcard {
    position: absolute; top: 172px;
    width: 560px; height: 400px;
    overflow: hidden;
    box-shadow: 0 10px 30px rgba(0,0,0,.6);
  }
  .postcard--front {
    left: 30px;
    background: radial-gradient(ellipse at 40% 40%, var(--card-grey) 0%, var(--card-grey-dark) 100%);
  }
  .postcard--back { left: 610px; background: var(--card-white); }

  .photo {
    position: absolute;
    border: 4px solid var(--photo-frame);
    box-shadow: 0 3px 8px rgba(0,0,0,.35);
  }
  .photo--venice    { left: 18px;  top: 18px;  width: 250px; height: 92px;
    background: linear-gradient(180deg, #8fb3da 0%, #c9a07a 45%, #b5775a 75%, #3f7f52 100%); }
  .photo--trevi     { left: 290px; top: 40px;  width: 175px; height: 110px;
    background: linear-gradient(180deg, #e7e3dc 0%, #cfc7ba 55%, #9a9387 100%); }
  .photo--colosseum { left: 40px;  top: 118px; width: 250px; height: 128px;
    background: linear-gradient(180deg, #b9cee6 0%, #c7ab82 45%, #8d6b48 80%, #6e8a45 100%); }
  .photo--car       { left: 190px; top: 258px; width: 132px; height: 104px;
    background: linear-gradient(160deg, #8d8a86 0%, #d62020 45%, #9a0d0d 75%, #5c5955 100%); }
  .photo--pisa      { left: 330px; top: 165px; width: 135px; height: 155px;
    background: linear-gradient(180deg, #3c79c2 0%, #8fb4de 45%, #ddd6c6 70%, #a79a86 100%); }

  .tyre-track {
    position: absolute;
    border-radius: 40%;
    background: radial-gradient(ellipse at center, var(--tyre-brown) 0%, rgba(150,132,112,0) 72%);
  }
  .postcard--front .tyre-track { right: 20px; top: 60px; width: 90px; height: 170px; transform: rotate(-14deg); }
  .postcard--back .tyre-track  { left: 20px; top: 160px; width: 100px; height: 200px; transform: rotate(-8deg); }

  .tour-tag {
    position: absolute; left: 418px; top: 206px; width: 134px; height: 120px;
    background: linear-gradient(135deg, var(--tag-paper) 0%, var(--tag-paper-dark) 100%);
    transform: rotate(-8deg);
    box-shadow: 0 3px 8px rgba(0,0,0,.35);
    color: var(--ink);
    padding: 10px 10px 0 14px;
    line-height: 1.05;
  }
  .tour-tag__title { font-size: 36px; display: block; }
  .tour-tag__line  { font-size: 19px; display: block; text-transform: uppercase; }

  .landmark-sketch {
    position: absolute;
    background: radial-gradient(ellipse at 60% 100%, var(--sketch-tone) 0%, rgba(60,55,50,0) 70%);
  }
  .postcard--front .landmark-sketch { right: 0; bottom: 0; width: 170px; height: 95px; }
  .postcard--back .landmark-sketch  { right: 0; bottom: 0; width: 130px; height: 70px; }

  .back-layout { position: absolute; inset: 0; }
  .back-message {
    position: absolute; left: 130px; top: 40px; width: 120px;
    color: var(--ink-soft); line-height: 1.2;
  }
  .back-message__theme { font-size: 17px; margin-bottom: 14px; }
  .back-message__call  { font-size: 14px; }
  .back-message__phone { display: block; font-size: 17px; color: var(--ink); margin: 4px 0; }
</style>
</head>
<body>
<main class="canvas">
  <section class="postcard postcard--front" aria-label="Postcard front">
    <div class="tyre-track" role="img" aria-label="Faint tyre track print"></div>
    <div class="photo photo--venice" role="img" aria-label="Photo of a Venetian canal with buildings"></div>
    <div class="photo photo--trevi" role="img" aria-label="Photo of the Trevi Fountain"></div>
    <div class="photo photo--colosseum" role="img" aria-label="Photo of the Colosseum in Rome"></div>
    <div class="photo photo--pisa" role="img" aria-label="Photo of the Leaning Tower of Pisa with a statue"></div>
    <div class="photo photo--car" role="img" aria-label="Photo of a red sports car"></div>
    <div class="landmark-sketch" role="img" aria-label="Line drawing of a classical monument"></div>
    <div class="tour-tag">
      <span class="tour-tag__title">Tour</span>
      <span class="tour-tag__line">Italy in a</span>
      <span class="tour-tag__line">Vellano"</span>
    </div>
  </section>

  <section class="postcard postcard--back" aria-label="Postcard back">
    <div class="tyre-track" role="img" aria-label="Faint tyre track print"></div>
    <div class="back-message">
      <p class="back-message__theme">A custom theme tour of Italy for your group with KWR Journeys.</p>
      <p class="back-message__call">Call <span class="back-message__phone">877-319-KWR7</span>(877-319-5977) for more details about our theme trips.</p>
    </div>
    <svg class="back-layout" width="560" height="400" viewBox="0 0 560 400" aria-hidden="true">
      <rect x="455" y="22" width="78" height="62" rx="12" fill="none" stroke="var(--line-grey)" stroke-width="2"/>
      <line x1="265" y1="60" x2="265" y2="350" stroke="var(--line-grey)" stroke-width="2" stroke-dasharray="2 4"/>
      <line x1="300" y1="170" x2="525" y2="170" stroke="var(--line-grey)" stroke-width="2"/>
      <line x1="300" y1="215" x2="525" y2="215" stroke="var(--line-grey)" stroke-width="2"/>
      <line x1="300" y1="260" x2="525" y2="260" stroke="var(--line-grey)" stroke-width="2"/>
    </svg>
    <div class="landmark-sketch" role="img" aria-label="Line drawing of a classical monument"></div>
  </section>
</main>
</body>
</html>
```